Home page makeover

Take my existing home page, www.maplecrestharborline.com and redesign layout to look more current considering today's touch design prevalence.
Reuse existing elements or suggest improved ones if available.
I generally have average CSS and HTML skills using div containers, defining lists and using columns to create the code to support the layout.
Updates
Just wanted to send out a quick message to thank all of you for your submissions. Many of you offered nice designs, but unfortunately could only choose one.
Target Market(s)
Generally targeting individuals with some assets for retirement. Basically your average working professional or business owner.
Industry/Entity Type
It Support
Look and feel
Each slider illustrates characteristics of the customer's brand and the style your logo design should communicate.

```html
<!DOCTYPE html>
<html lang="en">
<head>
<meta charset="utf-8">
<title>Maplecrest Retirement Planner – Home</title>
<link rel="stylesheet" href="https://fonts.googleapis.com/css2?family=Lato:ital,wght@0,300;0,400;1,900&amp;display=swap">
<style>
  :root {
    --header-green: #1f6e24;
    --hero-green: #6aa539;
    --hero-green-dark: #4f8a2a;
    --band-teal: #4dbf9c;
    --band-teal-dark: #35a385;
    --section-teal: #158260;
    --footer-dark: #1c1c1c;
    --white: #ffffff;
    --label-pink: #d23f7c;
    --label-teal: #3fbf98;
    --label-ink: #1e1e1e;
  }
  * { margin: 0; padding: 0; box-sizing: border-box; }
  html, body { width: 1108px; height: 1200px; overflow: hidden; }
  body {
    position: relative;
    font-family: "Lato", sans-serif;
    font-weight: 300;
    color: var(--white);
    background: var(--section-teal);
  }

  .site-header {
    position: absolute; left: 0; top: 0; width: 1108px; height: 63px;
    background: var(--header-green);
  }
  .brand { position: absolute; left: 124px; top: 12px; display: flex; align-items: center; gap: 12px; }
  .brand-mark { width: 24px; height: 24px; background: var(--white); }
  .brand-name { font-family: "Lato", sans-serif; font-size: 19px; font-weight: 400; }
  .brand-tagline {
    position: absolute; left: 160px; top: 38px;
    font-family: "Lato", sans-serif; font-size: 13px; font-weight: 300;
  }
  .main-nav { position: absolute; left: 668px; top: 36px; display: flex; }
  .main-nav a { color: var(--white); text-decoration: none; font-size: 15px; font-weight: 300; margin-right: 24px; }

  .hero {
    position: absolute; left: 0; top: 63px; width: 1108px; height: 368px;
    background: radial-gradient(ellipse at 60% 45%, var(--hero-green) 55%, var(--hero-green-dark) 100%);
  }
  .hero-video {
    position: absolute; left: 118px; top: 6px; width: 591px; height: 356px;
    background: linear-gradient(180deg, #e9b878 0%, #d89a55 35%, #6f8a92 55%, #c8b8a0 75%, #b77a45 100%);
  }
  .play-button { position: absolute; left: 239px; top: 126px; width: 113px; height: 93px; }
  .signup { position: absolute; left: 739px; top: 52px; }
  .signup-title { font-size: 43px; font-weight: 300; line-height: 1; margin-bottom: 34px; white-space: nowrap; }
  .signup-price { font-size: 20.5px; font-weight: 300; line-height: 26.5px; margin-bottom: 27px; white-space: nowrap; }

  .get-started {
    position: absolute; left: 0; top: 431px; width: 1108px; height: 252px;
    background: radial-gradient(ellipse at 50% 40%, var(--band-teal) 50%, var(--band-teal-dark) 100%);
  }
  .pointer { position: absolute; }
  .pointer-hero { left: 829px; top: 431px; }
  .pointer-band { left: 33px; top: 683px; }
  .get-started-title { position: absolute; left: 150px; top: 2px; font-size: 44px; font-weight: 400; }
  .step-tile { position: absolute; top: 56px; width: 287px; height: 184px; overflow: hidden; }
  .step-identify { left: 117px; background: linear-gradient(135deg, #cfd2db, #8c8fa0 60%, #5c5e6c); }
  .step-plan { left: 412px; background: linear-gradient(135deg, #a9a8b0, #3c3d44 55%, #d7c2b2); }
  .step-retire { left: 707px; background: linear-gradient(180deg, #d7a873 0%, #9db6b4 45%, #caa27a 100%); }
  .step-label { position: absolute; font-weight: 900; font-style: italic; font-size: 46px; }
  .step-identify .step-label { left: 118px; top: 68px; color: var(--label-ink); font-size: 44px; }
  .step-plan .step-label { left: 10px; top: 124px; color: var(--label-teal); }
  .step-retire .step-label { left: 20px; top: -2px; color: var(--label-pink); }

  .info { position: absolute; left: 0; top: 683px; width: 1108px; height: 369px; }
  .features { position: absolute; left: 164px; top: 22px; width: 290px; }
  .testimonials { position: absolute; left: 601px; top: 20px; width: 372px; }
  .section-title { font-size: 24px; font-weight: 300; margin-bottom: 14px; }
  .testimonials .section-title { font-size: 28px; margin-bottom: 18px; }
  .features p {
    font-size: 14.2px; line-height: 18px; text-indent: 12px; margin-bottom: 18px;
    letter-spacing: -0.3px; hyphens: auto;
  }
  .testimonials p {
    font-size: 18px; line-height: 22px; text-indent: 14px; margin-bottom: 22px;
    letter-spacing: -0.2px; hyphens: auto;
  }

  .site-footer {
    position: absolute; left: 0; top: 1052px; width: 1108px; height: 148px;
    background: var(--footer-dark);
  }
  .site-footer p {
    position: absolute; left: 117px; top: 14px; width: 876px;
    font-size: 15.8px; line-height: 20px; letter-spacing: -0.3px; hyphens: auto;
  }
</style>
</head>
<body>
  <header class="site-header">
    <div class="brand">
      <span class="brand-mark"></span>
      <span class="brand-name">Maplecrest Retirement Planner</span>
    </div>
    <span class="brand-tagline">It's Your Tommorrow</span>
    <nav class="main-nav">
      <a href="#">Home</a><a href="#">About</a><a href="#">Sign Up</a><a href="#">Contact</a><a href="#">Sign In</a>
    </nav>
  </header>

  <section class="hero">
    <div class="hero-video" role="img" aria-label="Video still: two striped beach chairs on the sand at sunset">
      <svg class="play-button" viewBox="0 0 113 93" aria-hidden="true">
        <rect width="113" height="93" fill="rgba(40,40,40,0.8)"/>
        <polygon points="40,22 40,72 84,47" fill="#d8d8d8"/>
      </svg>
    </div>
    <div class="signup">
      <h1 class="signup-title">Sign up now!</h1>
      <p class="signup-price">Only $19.99 For a<br>One Year<br>Membership</p>
      <p class="signup-price">Only $9.99 Per Year<br>After That</p>
    </div>
  </section>

  <section class="get-started">
    <h2 class="get-started-title">Get started!</h2>
    <div class="step-tile step-identify" role="img" aria-label="Calculator, cash and tax form on a desk">
      <span class="step-label">Identify</span>
    </div>
    <div class="step-tile step-plan" role="img" aria-label="Hands typing on a laptop keyboard">
      <span class="step-label">Plan</span>
    </div>
    <div class="step-tile step-retire" role="img" aria-label="Two striped beach chairs at the shoreline">
      <span class="step-label">Retire</span>
    </div>
  </section>

  <svg class="pointer pointer-hero" width="86" height="52" viewBox="0 0 86 52" aria-hidden="true">
    <polygon points="0,0 86,0 43,52" fill="#5f962f"/>
  </svg>

  <section class="info">
    <div class="features">
      <h3 class="section-title">FEATURES</h3>
      <p>Identify and project your retirement needs and expectations including basic living expenses, housing costs, recreation, big ticket non-recurring items, medical and nursing home care.</p>
      <p>Identify and project all your sources of retirement income including retirement savings, other savings, pension plans, Social Security, life insurance and working part-time during retirement for a period of time.</p>
      <p>Strategize tapping into the equity of your real estate including swapping your primary residence for a different home or retirement area, or selling and renting.</p>
    </div>
    <div class="testimonials">
      <h3 class="section-title">TESTIMONIALS</h3>
      <p>“This site is a great place to get a handle on your retirement strategy”, Dana, Oregon</p>
      <p>“It’s the only retirement projection tool for the average user that puts it all together”, Paul, Vermont</p>
      <p>“I can see professionals using this site to validate their existing retirement plans”, Paul, Vermont</p>
      <p>“Many people really need to do this”, Wendy,</p>
    </div>
  </section>

  <svg class="pointer pointer-band" width="78" height="52" viewBox="0 0 78 52" aria-hidden="true">
    <polygon points="0,0 78,0 39,52" fill="#3aa888"/>
  </svg>

  <footer class="site-footer">
    <p>We'd like to hear from you if you have any questions or comments regarding the content of this web-site. Just click on Contact above. Copyright 2013, Maplecrest Retirement Planner, Inc. All rights reserved. The "Retirement Compass" is a Trademark of Maplecrest Retirement Planner, Inc. All usage of this web-site is subject to the Terms and Conditions of Use you agreed to upon when accessing your user account. It should be duly noted that you will have no claim of any kind against Maplecrest Retirement Planner, Inc. as a byproduct of using this web-site and gaining results from it, especially if you reside, are employed or have assets held outside of the United States.</p>
  </footer>
</body>
</html>
```